Tin Lantern

I have written a book which I eventually would like to serve a couple of purposes. The initial purpose was to memorialize life events and lessons from my life to pass on to my grandchildren, in hopes they may learn from the experiences. As I completed the book, I now believe I could remove some of the family specific information as much of the information could be useful to many people.

While I want to book to have a great look for the grandkids, more importantly will be the version that we put on the bookshelf to sell. The cover is obviously the first thing a buyer will see and may or may not peak there interest. I would like to include the attached photo as the cover photo and the title language is also attached. Other than that I am not sure what is the best way to design the cover.

```html
<!DOCTYPE html>
<html lang="en">
<head>
<meta charset="utf-8">
<title>Tin Lantern – Lessons from my life to pass on to my grandchildren</title>
<link rel="stylesheet" href="https://fonts.googleapis.com/css2?family=Comic+Neue:ital,wght@0,400;0,700;1,400&family=Cabin:ital,wght@0,400;0,500;1,400&display=swap">
<style>
  :root {
    --green: #7db51f;
    --green-light: #94cc2c;
    --green-deep: #6aa313;
    --blue: #2fb0e8;
    --blue-light: #63d1f7;
    --orange: #f8a81a;
    --white: #ffffff;
    --ink: #1c1c1c;
    --photo-warm: #8a6a4e;
    --photo-cool: #6f8ea6;
  }
  * { margin: 0; padding: 0; box-sizing: border-box; }
  html, body { width: 1200px; height: 854px; overflow: hidden; background: var(--white); }
  .cover {
    position: relative; width: 1200px; height: 854px; overflow: hidden;
    font-family: "Cabin", Arial, sans-serif; color: var(--white);
  }
  .band { position: absolute; }
  .band--top { top: 0; height: 130px; background: var(--green); }
  .band--blue {
    top: 130px; height: 480px;
    background: linear-gradient(180deg, var(--blue-light) 0%, var(--blue) 100%);
    border-top: 3px solid var(--white);
  }
  .band--rule { top: 610px; height: 14px; background: var(--orange); }
  .band--bottom {
    top: 624px; height: 230px;
    background: radial-gradient(ellipse at 60% 30%, var(--green-light) 0%, var(--green) 60%, var(--green-deep) 100%);
  }
  .back .band { left: 0; width: 562px; }
  .front .band { left: 636px; width: 564px; }
  .front .band--top { height: 160px; }
  .front .band--blue { top: 160px; height: 450px; }

  .block { position: absolute; background: var(--green-light); opacity: .75; }

  .spine {
    position: absolute; left: 562px; top: 0; width: 74px; height: 854px;
    background: var(--orange);
    border-left: 3px solid var(--white); border-right: 3px solid var(--white);
  }
  .spine__title {
    position: absolute; left: 50%; top: 50%;
    transform: translate(-50%, -50%) rotate(-90deg);
    white-space: nowrap; font-size: 26px; color: var(--ink);
    font-family: "Cabin", Arial, sans-serif;
  }

  .photo {
    position: absolute; background: var(--white); padding: 7px;
    box-shadow: 3px 4px 8px rgba(0,0,0,.35);
  }
  .photo__fill {
    width: 100%; height: 100%;
    background: linear-gradient(160deg, var(--photo-cool) 0%, var(--photo-warm) 55%, #c9b79c 100%);
  }
  .photo--back { left: 142px; top: 78px; width: 290px; height: 186px; transform: rotate(-2deg); }
  .photo--front { left: 655px; top: 186px; width: 496px; height: 320px; transform: rotate(-1.5deg); }

  .blurb {
    position: absolute; left: 72px; top: 312px; width: 470px;
    font-style: italic; font-size: 16.5px; line-height: 1.3;
  }
  .blurb p + p { margin-top: 19px; }

  .author-badge {
    position: absolute; left: 320px; top: 512px; width: 200px; height: 200px;
    border-radius: 50%; background: var(--orange); border: 4px solid var(--white);
    display: flex; align-items: center; justify-content: center; text-align: center;
    font-family: "Comic Neue", cursive; font-weight: 700; font-size: 34px;
    line-height: 1.15; color: var(--ink);
  }

  .greeting {
    position: absolute; left: 668px; top: 34px;
    font-size: 48px; line-height: 1.1; font-weight: 500;
  }
  .names {
    position: absolute; left: 660px; top: 556px; width: 480px;
    text-align: center; font-size: 17px; line-height: 1.35;
    font-family: Arial, "Cabin", sans-serif;
  }

  .tagline {
    position: absolute; left: 666px; color: var(--ink);
    font-family: "Comic Neue", cursive; font-size: 20px; font-weight: 700;
  }
  .tagline--bump { top: 648px; }
  .tagline--life { top: 700px; }
  .tagline--great { top: 754px; }
  .tagline__life {
    font-size: 38px; color: var(--white); margin-left: 8px; letter-spacing: 1px;
    text-shadow: 1px 1px 0 var(--ink);
  }
  .tagline__aside {
    position: absolute; left: 288px; top: 14px; white-space: nowrap;
    font-size: 13px; font-weight: 400;
  }
  .signature {
    position: absolute; left: 966px; top: 782px; transform: rotate(-8deg);
    font-family: "Comic Neue", cursive; font-weight: 700; font-size: 24px;
    color: var(--white); text-shadow: 1px 1px 0 var(--ink), -1px -1px 0 var(--ink), 1px -1px 0 var(--ink), -1px 1px 0 var(--ink);
  }
</style>
</head>
<body>
<main class="cover">
  <section class="back">
    <div class="band band--top"></div>
    <div class="block" style="left:120px;top:0;width:240px;height:60px"></div>
    <div class="block" style="left:440px;top:20px;width:100px;height:90px"></div>
    <div class="band band--blue"></div>
    <div class="band band--rule"></div>
    <div class="band band--bottom"></div>

    <figure class="photo photo--back">
      <div class="photo__fill" role="img" aria-label="Family photo: grandfather sitting on a porch step with his seven grandsons"></div>
    </figure>

    <div class="blurb">
      <p>I was to memorialize life events</p>
      <p>and lessons from my life to pass on to my grandchildren,<br>in hopes they may learn from the experiences.<br>As I completed the book, I</p>
      <p>now believe I could remove some of the family specific<br>information as much of the information could be useful to<br>many people.</p>
    </div>

    <div class="author-badge">Grandpa<br>Norvik</div>
  </section>

  <aside class="spine">
    <h2 class="spine__title">Lessons from my life to pass on to my grandchildren</h2>
  </aside>

  <section class="front">
    <div class="band band--top"></div>
    <div class="block" style="left:940px;top:0;width:100px;height:120px"></div>
    <div class="block" style="left:1100px;top:95px;width:70px;height:65px"></div>
    <div class="band band--blue"></div>
    <div class="band band--rule"></div>
    <div class="band band--bottom"></div>

    <h1 class="greeting">Hi,<br>Guys……………</h1>

    <figure class="photo photo--front">
      <div class="photo__fill" role="img" aria-label="Family photo: grandfather sitting on a porch step with his seven grandsons"></div>
    </figure>

    <p class="names">Leo… Oliver… Milo… Owen… Elliot… Henry…<br>Theodore</p>

    <p class="tagline tagline--bump">There’s a bump in the road ahead……</p>
    <p class="tagline tagline--life">It’s called <span class="tagline__life">LIFE</span><span class="tagline__aside">(and life isn’t fair)</span></p>
    <p class="tagline tagline--great">This is about having a great one.</p>
    <p class="signature">Grandpa Norvik</p>
  </section>
</main>
</body>
</html>
```